New Wine Label - Classy, Simple, Modern

We are a small boutique winery who have been making and selling wine for 21 years. We are called "Velmora Winery" and Velmora is the Greek God of wine. We have a classic label at the moment that we would like to modernise.

We are looking to update our labels while keeping some of the original elements.
From existing label to definitely keep:
1. Logo (Colour can be darkened to a very dark purple - almost black)
2. Legal requirements - Front Label: 750ml, variety, year, "Canberra District" Back Label: Produce of Australia, number of standard drinks, alc/vol, additives, internet address, bar code plus new requirement to warn pregnant women alcohol can harm their babies.
From existing label open to change:
3. What would be nice - Separate front and back labels. Focus on logo on front label (Possibly printed in a raised gloss/embossed), Modern Font,
4. What can we lose? Happy to lose the words about us.
5.Font - Modern, Colour - white background, Shape Rectangular Front approximately height 11cm width 9cm & Back height 9cm width 7cm.

Prototype label can be for a
Front:
2022 Cabernet Sauvignon, Canberra District, 750ml, Estate Grown and Made
Back
13.6%ALC/VOL, APPROX 8.0 STANDARD DRINKS, PRESERVATIVE (220) ADDED, PRODUCE OF AUSTRALIA, Bar Code, Pregnant women warning, www.velmora-winery.com.au

if you want to use some words to describe the wine that's fine - you can make some up or use existing words from our website www.velmora-winery.com.au

Files:
1 - Photo of existing front label
2 - Current printers spec sheet for front and back label
3 - Pregnancy warning graphic (specific details see link below - label type 1)
4 - Current Bar Code for Cabernet Sauvignon
Many file types of existing logo

Link to legal requirement for pregnant women warning - we need label type 1 -https://www.tarvelcompliance.com.au/industry/labelling/Pages/pregnancy-warning-labels-downloadable-files.aspx

25 - 40 year olds, drink wine

Winery - Wine Production

```html
<!DOCTYPE html>
<html lang="en">
<head>
<meta charset="utf-8">
<title>Velmora Winery – Cabernet Sauvignon Front Label</title>
<link rel="stylesheet" href="https://fonts.googleapis.com/css2?family=Great+Vibes&family=Cinzel:wght@400;600&family=Montserrat:wght@500;600&display=swap">
<style>
  :root {
    --backdrop: #4a1729;
    --label-white: #ffffff;
    --band-purple: #2c1a5c;
    --band-purple-deep: #1f1245;
    --gold: #b8913f;
    --gold-light: #e2c27a;
    --gold-dark: #8c6a28;
    --ink: #2a2238;
    --ink-soft: #5c5668;
  }
  * { margin: 0; padding: 0; box-sizing: border-box; }
  html, body {
    width: 845px;
    height: 1200px;
    overflow: hidden;
    background: var(--backdrop);
  }
  .canvas {
    position: relative;
    width: 845px;
    height: 1200px;
  }
  .front-label {
    position: absolute;
    left: 102px;
    top: 100px;
    width: 640px;
    height: 1000px;
    background: var(--label-white);
    overflow: hidden;
  }
  .top-band {
    position: absolute;
    left: 0; top: 0;
    width: 100%;
    height: 225px;
    background: linear-gradient(180deg, var(--band-purple) 0%, var(--band-purple-deep) 100%);
  }
  .brand-mark {
    position: absolute;
    left: 50%;
    top: 140px;
    width: 170px;
    height: 170px;
    transform: translateX(-50%);
    border-radius: 50%;
    background: var(--band-purple-deep);
    border: 4px solid var(--gold);
  }
  .brand-name {
    position: absolute;
    top: 330px;
    width: 100%;
    text-align: center;
    font-family: "Cinzel", serif;
    font-weight: 400;
    font-size: 24px;
    letter-spacing: 2px;
    color: var(--ink-soft);
  }
  .variety {
    position: absolute;
    top: 385px;
    width: 100%;
    text-align: center;
    font-weight: normal;
  }
  .variety-script {
    display: block;
    padding: 40px 20px 12px;
    font-family: "Great Vibes", cursive;
    font-size: 128px;
    line-height: 1;
    color: var(--gold);
    background: linear-gradient(180deg, var(--gold-light) 20%, var(--gold) 60%, var(--gold-dark));
    -webkit-background-clip: text;
    background-clip: text;
    -webkit-text-fill-color: transparent;
  }
  .variety-caps {
    display: block;
    margin-top: -30px;
    padding: 0 20px 6px;
    font-family: "Cinzel", serif;
    font-weight: 600;
    font-size: 58px;
    line-height: 1.1;
    letter-spacing: 4px;
    color: var(--gold);
    background: linear-gradient(180deg, var(--gold-light), var(--gold) 55%, var(--gold-dark));
    -webkit-background-clip: text;
    background-clip: text;
    -webkit-text-fill-color: transparent;
  }
  .vintage {
    position: absolute;
    top: 650px;
    width: 100%;
    text-align: center;
    font-family: "Montserrat", sans-serif;
    font-weight: 600;
    font-size: 22px;
    letter-spacing: 8px;
    color: var(--ink);
  }
  .region {
    position: absolute;
    top: 760px;
    width: 100%;
    text-align: center;
    font-family: "Montserrat", sans-serif;
    font-weight: 500;
    font-size: 21px;
    letter-spacing: 3px;
    color: var(--ink);
  }
  .volume {
    position: absolute;
    top: 810px;
    width: 100%;
    text-align: center;
    font-family: "Montserrat", sans-serif;
    font-weight: 500;
    font-size: 13px;
    color: var(--ink-soft);
  }
  .gold-rule {
    position: absolute;
    left: 0;
    top: 868px;
    width: 100%;
    height: 3px;
    background: var(--gold);
  }
  .estate-band {
    position: absolute;
    left: 0;
    top: 880px;
    width: 100%;
    height: 66px;
    background: linear-gradient(90deg, var(--gold-dark), var(--gold-light) 45%, var(--gold) 70%, var(--gold-dark));
    display: flex;
    align-items: center;
    justify-content: center;
  }
  .estate-text {
    font-family: "Montserrat", sans-serif;
    font-weight: 600;
    font-size: 17px;
    letter-spacing: 6px;
    color: var(--band-purple-deep);
  }
  .warning-mark {
    position: absolute;
    right: 34px;
    top: 50%;
    width: 30px;
    height: 30px;
    transform: translateY(-50%);
    background: var(--band-purple-deep);
  }
</style>
</head>
<body>
  <main class="canvas">
    <section class="front-label">
      <div class="top-band"></div>
      <div class="brand-mark"></div>
      <p class="brand-name">Velmora Winery</p>

      <h1 class="variety">
        <span class="variety-script">Cabernet</span>
        <span class="variety-caps">Sauvignon</span>
      </h1>
      <p class="vintage">2022</p>

      <p class="region">CANBERRA DISTRICT</p>
      <p class="volume">750ml</p>

      <div class="gold-rule"></div>
      <div class="estate-band">
        <span class="estate-text">ESTATE GROWN AND MADE</span>
        <span class="warning-mark" role="img" aria-label="Pregnancy warning symbol"></span>
      </div>
    </section>
  </main>
</body>
</html>
```